New Business Card Design Project

Use the flyer uploaded and website www.brightoakbuilders.com for inspiration.
List Our Services on Backside of business cards
Martin Hollis
Harborline Renovations Inc.
Licensed General Contractors
858-471-9063

Contact Information for Business Card

Use the flyer uploaded and website www.brightoakbuilders.com for inspiration. List Our Services on Backside of business cards Martin Hollis Harborline Renovations Inc. Licensed General Contractors 858-471-9063

```html
<!DOCTYPE html>
<html lang="en">
<head>
<meta charset="utf-8">
<title>Harborline Renovations – Business Card</title>
<link href="https://fonts.googleapis.com/css2?family=Roboto:wght@300;400;700&family=Roboto+Condensed:wght@700&display=swap" rel="stylesheet">
<style>
  :root {
    --backdrop: #2b2b2b;
    --card: #353535;
    --card-edge: #404040;
    --ink: #f2f2f2;
    --ink-soft: #cfcfcf;
    --rule: #8a8a8a;
    --art-light: #5a5a5a;
    --art-dark: #3d3d3d;
  }
  * { box-sizing: border-box; margin: 0; padding: 0; }
  html, body { width: 1200px; height: 689px; overflow: hidden; background: var(--backdrop); }
  body { font-family: "Roboto", Arial, sans-serif; color: var(--ink); position: relative; }

  .card {
    position: absolute; top: 190px; width: 540px; height: 309px;
    background: var(--card); border: 1px solid var(--card-edge); border-radius: 16px;
    overflow: hidden;
  }
  .card--back { left: 40px; }
  .card--front { left: 620px; }

  /* Back side */
  .services-art {
    position: absolute; left: 150px; top: 22px; width: 240px; height: 170px;
    border-radius: 8px;
    background: radial-gradient(ellipse at 55% 35%, var(--art-light), var(--art-dark) 75%);
  }
  .services {
    position: absolute; left: 24px; right: 24px; top: 204px;
    border-top: 1px solid var(--rule); border-bottom: 1px solid var(--rule);
    padding: 9px 0; text-align: center; font-size: 12.5px; line-height: 1.45; color: var(--ink);
  }
  .services b { font-weight: 700; }

  /* Front side */
  .brand {
    position: absolute; left: 24px; top: 0; width: 250px; height: 250px;
    display: flex; align-items: center; justify-content: center; gap: 10px;
  }
  .brand__mark { width: 14px; height: 14px; border: 1.5px solid var(--ink); flex: none; }
  .brand__name { font-weight: 300; font-size: 19px; letter-spacing: 1.5px; text-transform: uppercase; color: var(--ink); line-height: 1.3; }
  .divider { position: absolute; left: 290px; top: 40px; height: 170px; width: 1px; background: var(--rule); }
  .contact { position: absolute; left: 310px; top: 44px; }
  .contact__name { font-family: "Roboto Condensed", "Arial Narrow", sans-serif; font-weight: 700; font-size: 26px; letter-spacing: .5px; text-transform: uppercase; }
  .contact__title { font-size: 13px; color: var(--ink-soft); margin-top: 2px; }
  .contact__list { list-style: none; margin-top: 20px; font-size: 13.5px; }
  .contact__list li { display: flex; align-items: center; gap: 9px; margin-bottom: 6px; }
  .contact__list svg { width: 12px; height: 12px; fill: var(--ink); flex: none; }
  .legal {
    position: absolute; left: 0; right: 0; bottom: 26px; text-align: center;
    font-size: 13.5px; color: var(--ink);
  }
</style>
</head>
<body>
  <section class="card card--back" aria-label="Back of business card">
    <div class="services-art" role="img" aria-label="Line illustration of a palm tree rising over a house outline"></div>
    <p class="services">
      <b>Remodel :</b> Kitchen &amp; Bath | <b>Painting :</b> Interior &amp; Exterior | <b>Flooring :</b> Carpet, Vinyl, Wood<br>
      Window &amp; Door Replacement | <b>Plumbing :</b> Repairs &amp; Upgrades | Energy- Efficient Upgrades<br>
      Deck &amp; Patio Construction | Water &amp; Mold Damage | Garage Renovation
    </p>
  </section>

  <section class="card card--front" aria-label="Front of business card">
    <div class="brand">
      <span class="brand__mark"></span>
      <span class="brand__name">Harborline<br>Renovations</span>
    </div>
    <div class="divider"></div>
    <div class="contact">
      <h1 class="contact__name">Martin Hollis</h1>
      <p class="contact__title">President</p>
      <ul class="contact__list">
        <li><svg viewBox="0 0 24 24"><path d="M6.6 10.8a15 15 0 0 0 6.6 6.6l2.2-2.2a1 1 0 0 1 1-.25 11.4 11.4 0 0 0 3.6.57 1 1 0 0 1 1 1V20a1 1 0 0 1-1 1A17 17 0 0 1 3 4a1 1 0 0 1 1-1h3.5a1 1 0 0 1 1 1c0 1.25.2 2.45.57 3.57a1 1 0 0 1-.25 1z"/></svg>858-471-9063</li>
        <li><svg viewBox="0 0 24 24"><path d="M2 5h20v14H2z M2 5l10 8 10-8" /></svg>info@brightoakbuilders.com</li>
        <li><svg viewBox="0 0 24 24"><circle cx="12" cy="12" r="10"/></svg>www.brightoakbuilders.com</li>
      </ul>
    </div>
    <p class="legal">Harborline Renovations Inc.&nbsp; | &nbsp;Licensed General Contractors</p>
  </section>
</body>
</html>
```